Moravel Stenwick Inc needs a business card design

Looking for a unique, classy and sharp business card design.

Contact Information for Business Card

Moravel Stenwick Inc.
Marisa Ortega Bellido BScOT(c)
Occupational Therapist
(780) 555-0142
moravelstenwick@postlynx.net

```html
<!DOCTYPE html>
<html lang="en">
<head>
<meta charset="utf-8">
<title>Moravel Stenwick Inc. — Business Card</title>
<link href="https://fonts.googleapis.com/css2?family=Questrial&display=swap" rel="stylesheet">
<style>
  :root {
    --backdrop: #202020;
    --card: #ffffff;
    --purple: #8b2a8f;
    --green: #8cc63f;
    --text-grey: #5a5a5a;
    --faint: #eef3e8;
    --rule-top: #b8e07a;
    --rule-bottom: #c77fc9;
  }
  * { margin: 0; padding: 0; box-sizing: border-box; }
  html, body {
    width: 1200px; height: 852px; overflow: hidden;
    background: var(--backdrop);
    font-family: "Questrial", "Century Gothic", sans-serif;
  }
  .stage { position: relative; width: 1200px; height: 852px; }
  .card {
    position: absolute;
    width: 520px; height: 300px;
    background: var(--card);
    border-radius: 22px;
    overflow: hidden;
    box-shadow: 0 10px 30px rgba(0,0,0,0.5);
  }
  .card--front { left: 80px; top: 110px; }
  .card--back { left: 600px; top: 442px; }

  .decor-mark {
    position: absolute;
    border-radius: 50%;
    background: var(--faint);
    opacity: 0.8;
  }
  .card--front .decor-mark { width: 220px; height: 220px; right: -40px; top: -50px; }
  .card--back .decor-mark { width: 240px; height: 240px; right: -50px; top: -40px; }

  .brand {
    position: absolute;
    display: flex; align-items: center; gap: 10px;
  }
  .brand__dot {
    width: 26px; height: 26px; border-radius: 50%;
    background: var(--green); flex: none;
  }
  .brand__name {
    color: var(--purple);
    font-size: 26px; line-height: 1.05;
    width: 170px;
  }
  .card--front .brand { left: 150px; top: 112px; }
  .card--back .brand { left: 40px; top: 116px; }
  .card--back .brand__name { font-size: 22px; width: 150px; }

  .divider {
    position: absolute; left: 245px; top: 92px;
    width: 1.5px; height: 120px;
    background: linear-gradient(var(--rule-top), var(--rule-bottom));
  }
  .details { position: absolute; left: 262px; top: 96px; }
  .details__name { color: var(--purple); font-size: 14.5px; }
  .details__title { color: var(--green); font-size: 14px; margin-top: 2px; }
  .details__row {
    display: flex; align-items: center; gap: 7px;
    color: var(--text-grey); font-size: 13.5px; margin-top: 7px;
  }
  .details__row:first-of-type { margin-top: 9px; }
  .icon {
    width: 15px; height: 15px; border-radius: 50%;
    background: var(--green);
    display: flex; align-items: center; justify-content: center; flex: none;
  }
</style>
</head>
<body>
<main class="stage">
  <section class="card card--front" aria-label="Card front">
    <div class="decor-mark" aria-hidden="true"></div>
    <div class="brand">
      <span class="brand__dot"></span>
      <span class="brand__name">Moravel Stenwick Inc.</span>
    </div>
  </section>

  <section class="card card--back" aria-label="Card back">
    <div class="decor-mark" aria-hidden="true"></div>
    <div class="brand">
      <span class="brand__dot"></span>
      <span class="brand__name">Moravel Stenwick Inc.</span>
    </div>
    <div class="divider"></div>
    <div class="details">
      <p class="details__name">Marisa Ortega Bellido BScOT(c)</p>
      <p class="details__title">Occupational Therapist</p>
      <p class="details__row">
        <span class="icon">
          <svg width="9" height="9" viewBox="0 0 24 24"><path fill="#fff" d="M6.6 10.8a15 15 0 0 0 6.6 6.6l2.2-2.2a1 1 0 0 1 1-.25 11.4 11.4 0 0 0 3.6.57 1 1 0 0 1 1 1V20a1 1 0 0 1-1 1A17 17 0 0 1 3 4a1 1 0 0 1 1-1h3.5a1 1 0 0 1 1 1c0 1.25.2 2.45.57 3.57a1 1 0 0 1-.25 1z"/></svg>
        </span>
        (780) 555-0142
      </p>
      <p class="details__row">
        <span class="icon">
          <svg width="9" height="9" viewBox="0 0 24 24"><path fill="#fff" d="M2 5h20v14H2z"/><path fill="none" stroke="#8cc63f" stroke-width="2" d="M2 5l10 8 10-8"/></svg>
        </span>
        moravelstenwick@postlynx.net
      </p>
    </div>
  </section>
</main>
</body>
</html>
```